Mailer Postcard for Potential Bankruptcy Clients

The postcard will be printed at 8.5"x6" to abide by the specification at the following link: https://www.mailvortex.example/art-upload/guide/. I want an attractive two sided post card that includes my logo (see attachment). The design would have to have room for the website address, phone number, two location addresses and give them information about a civil action pending against them (You are being sued in X county (case# xxyx). We can help.). I don't really like the visuals of the attached postcard, so please use as a general guide for what I am trying to do. Ultimately, I want an ad that gets people to call me so I can help them.

I also want it to be compatible with the website (CreditHarbor.Legal).

Target Market(s)

Potential bankruptcy clients.

Industry/Entity Type

Legal

Colors

Designer to choose colors to be used in the design.

Requirements
Must have
• Phone number, addresses, website, and place for text regarding pending legal action against the receiver. Should say something to the effect: You have a pending legal action in (county name) County (court name [superior, magistrate, ect.]). Let us help you deal with it responsibly.
• Please note the design specifications at this link:

```html
<!DOCTYPE html>
<html lang="en">
<head>
<meta charset="utf-8">
<title>Credit Harbor Law Group – Mailer Postcard</title>
<link rel="stylesheet" href="https://fonts.googleapis.com/css2?family=Raleway:wght@500;600;700;800&family=Open+Sans:ital,wght@0,400;0,600;0,700;1,600&display=swap">
<style>
:root{
  --green:#7dbb80;
  --green-deep:#5da462;
  --green-light:#a6d3a8;
  --charcoal:#333536;
  --charcoal-dark:#262829;
  --ink:#2b2b2b;
  --white:#ffffff;
  --grey-box:#dcdcdc;
  --backdrop:#e8e6e2;
}
*{box-sizing:border-box;margin:0;padding:0}
html,body{width:902px;height:1200px;overflow:hidden}
body{background:var(--backdrop);font-family:"Open Sans",Arial,sans-serif;color:var(--ink);position:relative}
.card{position:absolute;left:74px;width:754px;height:488px;background:var(--white);overflow:hidden;box-shadow:0 3px 10px rgba(0,0,0,.18)}
.front{top:110px}
.back{top:640px}
.abs{position:absolute}

/* FRONT */
.front-hero{left:0;top:0;width:754px;height:295px;background:linear-gradient(90deg,#2b2d2e 0%,#3a3c3d 55%,#4a4c4c 100%)}
.hero-photo{left:460px;top:0;width:294px;height:295px;background:radial-gradient(ellipse at 60% 50%,#6d6f70 0%,#45484a 55%,rgba(58,60,61,0) 100%)}
.feature-photo{left:38px;top:14px;width:304px;height:338px;border:6px solid var(--green);border-radius:14px 14px 60px 60px;background:radial-gradient(circle at 50% 45%,#3f6a86 0%,#1f3a50 50%,#16222e 100%)}
.headline{left:366px;top:18px;font-family:"Raleway",sans-serif;font-weight:700;font-size:31px;line-height:36px;color:var(--white);letter-spacing:.3px}
.headline .accent{color:var(--green)}
.benefits{left:368px;top:95px;list-style:none;font-style:italic;font-weight:600;font-size:12px;color:var(--white)}
.benefits li{height:19.4px;line-height:19.4px;padding-left:21px;position:relative}
.benefits li::before{content:"";position:absolute;left:0;top:5px;width:9px;height:9px;border-radius:50%;background:var(--green-light)}
.white-strip{left:0;top:295px;width:754px;height:15px;background:var(--white)}
.dark-band{left:0;top:310px;width:754px;height:28px;background:var(--charcoal)}
.appointment{left:370px;top:300px;width:326px;height:93px;border-radius:3px;background:linear-gradient(180deg,var(--green) 0%,var(--green) 36%,#e9f3e9 40%,#b9dcbb 100%);box-shadow:0 3px 6px rgba(0,0,0,.25)}
.appointment-title{left:0;top:8px;width:326px;text-align:center;font-family:"Raleway",sans-serif;font-weight:600;font-size:19px;color:var(--white)}
.appointment-phone{left:10px;top:40px;display:flex;align-items:center;gap:8px;font-family:"Raleway",sans-serif;font-weight:700;font-size:34px;color:var(--ink)}
.info-lead{left:370px;top:404px;width:326px;text-align:center;font-family:"Raleway",sans-serif;font-weight:700;font-size:16px;color:var(--ink)}
.info-url{left:370px;top:427px;width:326px;text-align:center;font-family:"Raleway",sans-serif;font-weight:600;font-size:16px;letter-spacing:2.6px;color:var(--ink)}
.brand{display:flex;align-items:center;gap:9px}
.brand-mark{background:var(--green)}
.brand-name{font-family:"Raleway",sans-serif;font-weight:600;color:var(--charcoal)}
.front .brand{left:100px;top:364px}
.front .brand-mark{width:30px;height:30px}
.front .brand-name{font-size:22px;line-height:25px}
.brand-sub{font-family:"Raleway",sans-serif;font-weight:600;color:var(--charcoal)}
.front .brand-sub{left:139px;top:391px;font-size:10px;letter-spacing:2px}
.front .brand-by{left:139px;top:405px;font-size:8px;font-style:italic;color:var(--green-deep)}
.disclaimer{left:20px;top:437px;font-weight:600;font-size:8.6px;color:var(--ink)}
.green-foot{left:0;top:460px;width:754px;height:28px;background:var(--green)}

/* BACK */
.back-left{left:0;top:0;width:394px;height:488px;background:var(--charcoal)}
.stress-photo{left:0;top:0;width:168px;height:150px;background:linear-gradient(135deg,#f4f4f4 0%,#dadada 60%,#c4c4c4 100%)}
.pending{left:168px;top:0;width:212px;height:99px;background:var(--green);padding:17px 0 0 9px}
.pending-title{font-family:"Raleway",sans-serif;font-weight:600;font-size:10.5px;color:var(--white);white-space:nowrap}
.field{display:flex;align-items:center;margin-top:8px;font-family:"Raleway",sans-serif;font-weight:600;font-size:7.5px;color:var(--white)}
.field span{width:64px}
.field i{display:block;width:128px;height:13px;background:var(--white)}
.help{left:168px;top:99px;width:212px;height:52px;background:#ececec;padding:5px 0 0 10px;font-family:"Raleway",sans-serif;font-weight:500;font-size:15.5px;line-height:19px;color:var(--ink);white-space:nowrap}
.about{left:0;top:152px;width:380px;height:122px;background:var(--green);padding:4px 0 0 18px}
.section-title{font-family:"Raleway",sans-serif;font-weight:700;font-size:12px;line-height:15px;color:var(--white)}
.about p{font-size:7.4px;line-height:9.6px;color:var(--white);text-align:justify;width:294px;margin-top:1px}
.divider-strip{left:380px;top:0;width:14px;height:488px;background:var(--charcoal-dark)}
.team-photo{left:320px;top:140px;width:142px;height:154px;border:5px solid var(--white);box-shadow:0 0 0 2px var(--charcoal);border-radius:10px 10px 50px 50px;background:linear-gradient(160deg,#f2f4f6 0%,#cfd8e2 55%,#9fb2c6 100%)}
.services{left:0;top:274px;width:380px;height:104px;background:linear-gradient(90deg,#ffffff 55%,#ededed 100%);padding:4px 0 0 18px}
.services .section-title{color:var(--green-deep)}
.services-lead{font-weight:600;font-size:8.6px;line-height:12px;color:var(--ink);width:345px}
.service-cols{display:flex;gap:42px;margin-top:8px}
.service-cols ul{list-style:none;font-style:italic;font-weight:600;font-size:8.2px;color:var(--ink)}
.service-cols li{height:14.5px;padding-left:12px;position:relative}
.service-cols li::before{content:"";position:absolute;left:0;top:3px;width:5px;height:5px;border-radius:50%;background:var(--green)}
.locations{left:0;top:378px;width:380px;height:110px;background:var(--charcoal-dark);padding:7px 0 0 18px}
.locations-lead{font-family:"Raleway",sans-serif;font-weight:600;font-size:8.5px;color:var(--green-light)}
.addresses{display:flex;margin-top:10px}
.address{display:flex;gap:6px;font-weight:600;font-size:7.4px;line-height:10px;color:var(--white);width:175px}
.address + .address{border-left:1px solid #5a5c5d;padding-left:8px;width:170px}
.contact-row{display:flex;align-items:center;margin-top:14px;gap:6px;color:var(--white)}
.contact-phone{font-family:"Raleway",sans-serif;font-weight:700;font-size:19px}
.contact-url{font-family:"Raleway",sans-serif;font-weight:700;font-size:14px;margin-left:10px;border-left:1px solid #5a5c5d;padding-left:8px;display:flex;align-items:center;gap:5px}
.back .brand{left:418px;top:38px;flex-direction:column;gap:4px;align-items:center}
.back .brand-mark{width:22px;height:22px}
.back .brand-name{font-size:12px}
.back .brand-sub{font-size:6px;letter-spacing:1.5px}
.stamp-box{left:630px;top:24px;width:102px;height:96px;background:var(--grey-box)}
.address-box{left:423px;top:286px;width:309px;height:163px;background:var(--grey-box)}
</style>
</head>
<body>

<section class="card front" aria-label="Postcard front">
  <div class="abs front-hero"></div>
  <div class="abs hero-photo" role="img" aria-label="Photo of a relieved man in a shirt and tie stretching his arms wide"></div>
  <div class="abs feature-photo" role="img" aria-label="Photo of a businessman's hands cupped around a glowing dollar sign"></div>

  <h1 class="abs headline">GET OUT OF DEBT AND<br><span class="accent">RESTORE YOUR CREDIT</span></h1>
  <ul class="abs benefits">
    <li>$0 Down Bankruptcy Options</li>
    <li>Student Loan Representation</li>
    <li>Stop Lawsuits</li>
    <li>Stop Collection Calls</li>
    <li>Stop Foreclosures &amp; Repossessions</li>
    <li>Stop Garnishments</li>
    <li>Free Credit Education Program</li>
    <li>Fix Credit Report Errors</li>
    <li>Prosecute Illegal Debt Collection Practices</li>
    <li>Prosecute Post Discharge Violations</li>
  </ul>

  <div class="abs white-strip"></div>
  <div class="abs dark-band"></div>

  <div class="abs appointment">
    <div class="abs appointment-title">Schedule Appointment</div>
    <div class="abs appointment-phone">
      <svg width="28" height="28" viewBox="0 0 28 28" aria-hidden="true"><circle cx="14" cy="14" r="12.5" fill="none" stroke="#2b2b2b" stroke-width="2"/><path d="M10 7.5c1 0 1.6 2.6 1.6 3.4 0 .9-1.3 1.2-1.1 2 .5 1.8 2.3 3.6 4 4.1.8.2 1.1-1.1 2-1.1.8 0 3.4.6 3.4 1.6 0 1.4-1.4 3-3 3-4.6 0-9.9-5.3-9.9-9.9 0-1.6 1.6-3.1 3-3.1z" fill="#2b2b2b"/></svg>
      (404) 555-0187
    </div>
  </div>
  <div class="abs info-lead">For more information visit us:</div>
  <div class="abs info-url">www.CreditHarbor.legal</div>

  <div class="abs brand"><span class="brand-mark"></span><span class="brand-name">Credit Harbor</span></div>
  <div class="abs brand-sub">LAW GROUP</div>
  <div class="abs brand-sub brand-by">by Attorney M. Calloway</div>
  <p class="abs disclaimer">We are a federally designated Debt Relief Agency. Paid Attorney Advertisement.</p>
  <div class="abs green-foot"></div>
</section>

<section class="card back" aria-label="Postcard back">
  <div class="abs back-left"></div>
  <div class="abs divider-strip"></div>
  <div class="abs stress-photo" role="img" aria-label="Photo of a stressed man holding his head, surrounded by words like debt, loss and pain"></div>

  <div class="abs pending">
    <div class="pending-title">YOU HAVE A PENDING LEGAL ACTION IN</div>
    <div class="field"><span>COUNTY NAME :</span><i></i></div>
    <div class="field"><span>COURT NAME :</span><i></i></div>
  </div>
  <div class="abs help">LET US HELP YOU DEAL<br>WITH IT RESPONSIBLY</div>

  <div class="abs about">
    <h2 class="section-title">WHO ARE WE?</h2>
    <p>We are a Georgia Law Firm dedicated to being a valuable resource for all of the debt woes that ordinary people face. We are experienced bankruptcy attorneys with litigation experience that understand that people need more than just your typical bankruptcy lawyer. People need someone that is experienced in handling all of the practical aspects of avoiding bankruptcy, recovering from bankruptcy quickly, tackling stubborn student loans, and punishing abusive debt collectors in court when they violate the law. Let us help you navigate your options and find a solution for your troubling debt.</p>
  </div>

  <div class="abs services">
    <h2 class="section-title">OUR SERVICES</h2>
    <p class="services-lead">Below are a few services that we offer. Contact us to get more details and see what we can do for you.</p>
    <div class="service-cols">
      <ul><li>Mortgage Loan Modifications</li><li>Credit Report Inaccuracies &amp; Errors</li><li>Student Loans</li></ul>
      <ul><li>Debt Collection Violations</li><li>Bankruptcy</li><li>Free Credit Rebuilding Program</li></ul>
    </div>
  </div>

  <div class="abs locations">
    <div class="locations-lead">We're located in the heart of downtown Atlanta, GA, and historic Douglasville, GA at:</div>
    <div class="addresses">
      <div class="address">
        <svg width="7" height="10" viewBox="0 0 7 10" aria-hidden="true"><path d="M3.5 0A3.5 3.5 0 0 0 0 3.5C0 6 3.5 10 3.5 10S7 6 7 3.5A3.5 3.5 0 0 0 3.5 0zm0 5a1.4 1.4 0 1 1 0-2.8 1.4 1.4 0 0 1 0 2.8z" fill="#a6d3a8"/></svg>
        <span>418 Linden Ave., NW Suite #1200<br>Atlanta, Georgia 30303</span>
      </div>
      <div class="address">
        <svg width="7" height="10" viewBox="0 0 7 10" aria-hidden="true"><path d="M3.5 0A3.5 3.5 0 0 0 0 3.5C0 6 3.5 10 3.5 10S7 6 7 3.5A3.5 3.5 0 0 0 3.5 0zm0 5a1.4 1.4 0 1 1 0-2.8 1.4 1.4 0 0 1 0 2.8z" fill="#a6d3a8"/></svg>
        <span>2150 W. Maple St.<br>Douglasville, GA 30134</span>
      </div>
    </div>
    <div class="contact-row">
      <svg width="14" height="14" viewBox="0 0 28 28" aria-hidden="true"><circle cx="14" cy="14" r="12.5" fill="none" stroke="#a6d3a8" stroke-width="2.5"/><path d="M10 7.5c1 0 1.6 2.6 1.6 3.4 0 .9-1.3 1.2-1.1 2 .5 1.8 2.3 3.6 4 4.1.8.2 1.1-1.1 2-1.1.8 0 3.4.6 3.4 1.6 0 1.4-1.4 3-3 3-4.6 0-9.9-5.3-9.9-9.9 0-1.6 1.6-3.1 3-3.1z" fill="#a6d3a8"/></svg>
      <span class="contact-phone">(404) 555-0187</span>
      <span class="contact-url">
        <svg width="12" height="12" viewBox="0 0 12 12" aria-hidden="true"><g fill="none" stroke="#a6d3a8" stroke-width="1"><circle cx="6" cy="6" r="5.3"/><ellipse cx="6" cy="6" rx="2.4" ry="5.3"/><path d="M.7 6h10.6M1.6 3.3h8.8M1.6 8.7h8.8"/></g></svg>
        www.CreditHarbor.legal
      </span>
    </div>
  </div>

  <div class="abs team-photo" role="img" aria-label="Photo of a smiling couple shaking hands with an attorney in an office"></div>

  <div class="abs brand">
    <span class="brand-mark"></span>
    <span class="brand-name">Credit Harbor</span>
    <span class="brand-sub">LAW GROUP</span>
  </div>
  <div class="abs stamp-box"></div>
  <div class="abs address-box"></div>
</section>

</body>
</html>
```